PLNT VRSE

We're a creative firm who connects content with clients.
I am looking to build a membership site where free users will upload content in either video, audio, written or picture format, and clients can choose to purchase said content through the site.
3 levels of membership - free users (who can upload content), paid users (who can browse and purchase content) and admin (my team, who can liaise between the two and shuffle content around and edit descriptions of that content).
Can this even be done!?

I'll just ask for a design at this stage, then once I've selected it I can work with you to progress into a fully functioning site if that works?

For paid users I would like it to have a square-tile look- similar to daysandhours.example (although I don't like Kilo-B, I much prefer Rue).

I'd like to be able to edit the site's content myself, so even if you were to design the site through something like tilo? I'm new to this so let me know if I'm being ridiculus.

Target Market(s)

15-50yr old. Creatives, designers, advertisers.

Industry/Entity Type

Advertising

Number of Pages Required

5+ page

Font styles to use
Sans Serif

Requirements
Must have
• 3 levels of access/membership
• Coinbay

```html
<!DOCTYPE html>
<html lang="en">
<head>
<meta charset="utf-8">
<title>PLNT VRSE — Content</title>
<link href="https://fonts.googleapis.com/css2?family=Mulish:wght@400;600;700;800&display=swap" rel="stylesheet">
<style>
:root{
  --bg-page:#393a3f;
  --bg-bar:#2b2c30;
  --bg-panel:#2f3035;
  --bg-dark:#222326;
  --line:#3f4045;
  --green:#21b36b;
  --text:#ffffff;
  --muted:#a9abb0;
  --dim:#7c7e84;
}
*{box-sizing:border-box;margin:0;padding:0}
html,body{width:738px;height:1200px;overflow:hidden}
body{position:relative;background:var(--bg-page);font-family:"Mulish",sans-serif;color:var(--text);font-size:8px}
.abs{position:absolute}
.header{left:0;top:0;width:738px;height:30px;background:var(--bg-bar)}
.header .nav{top:10px;font-size:7.5px;color:var(--text)}
.header .sep{left:95px;top:9px;width:1px;height:11px;background:var(--dim)}
.wordmark{display:flex;align-items:center;gap:6px;font-weight:600;letter-spacing:.6px;color:var(--text)}
.wordmark .mark{width:8px;height:8px;background:var(--green)}
.header .wordmark{left:0;width:738px;justify-content:center;top:7px;font-size:14px}
.btn{background:var(--green);color:#fff;font-weight:700;text-align:center;border-radius:1px}
.header .signup{left:623px;top:7px;width:60px;height:15px;line-height:15px;font-size:7.5px}

.gallery{left:0;top:30px;width:738px;height:320px;background:var(--bg-dark)}
.tile{position:absolute;width:100px;height:100px}
.tile.part{width:50px}
.arrow{position:absolute;color:var(--green);font-size:12px;font-weight:700}

.card{background:var(--green);color:#fff}
.card .type{left:8px;top:5px;font-size:6px;display:flex;gap:10px;align-items:center}
.card .name{left:8px;top:27px;font-size:7px;font-weight:700}
.card .by{left:8px;top:38px;font-size:5.5px;color:#c8f0da}
.card .date{left:8px;top:87px;font-size:6px}
.card .icons{right:8px;top:86px;font-size:7px;font-weight:800;display:flex;gap:5px;align-items:center}

.tabs{left:0;top:350px;width:738px;height:31px;background:var(--bg-bar)}
.tab{top:11px;font-size:8px;color:var(--dim)}
.tab.active{color:#fff}
.tab-line{left:55px;top:28px;width:24px;height:2px;background:var(--green)}
.search{left:564px;top:9px;width:118px;height:15px;background:#fff}

.panel{background:var(--bg-panel)}
.main{left:55px;top:398px;width:467px;height:378px}
.main .meta{left:16px;top:9px;font-size:7px;color:#d8d9dc}
.dots{display:flex;gap:4px;position:absolute}
.dot{width:6px;height:6px;border-radius:50%;background:#e6e6e6}
.video{left:0;top:26px;width:467px;height:264px;background:linear-gradient(180deg,#3d8fa6 0%,#6fb3c4 35%,#8dbfcb 48%,#2f7f9a 60%,#1d5e7c 100%)}
.play{left:213px;top:113px;width:40px;height:40px;background:#000}
.main .title{left:16px;top:298px;font-size:14px;font-weight:700}
.main .rule{left:0;width:467px;height:1px;background:var(--line)}
.main .desc{left:16px;top:341px;width:440px;font-size:6.6px;line-height:10px;color:#d2d3d6}
.main .more{left:16px;top:362px;font-size:5.5px;color:var(--green)}

.side{left:527px;top:398px;width:155px;height:378px}
.side .rule{left:0;width:155px;height:1px;background:var(--line)}
.stats{left:10px;top:9px;font-size:7px;font-weight:700;display:flex;gap:10px}
.buy{left:10px;top:42px;width:134px;height:15px;line-height:15px;font-size:6.5px}
.tag{position:absolute;border:1px solid #d0d0d0;font-size:6.5px;font-weight:700;padding:2px 5px;height:15px}
.action{display:flex;align-items:center;gap:8px;font-size:7px;font-weight:700;top:155px}
.action .sq{width:19px;height:19px;background:var(--green);display:flex;align-items:center;justify-content:center}
.side .from{left:10px;top:194px;font-size:7px;font-weight:700}
.side .from span{font-weight:400;color:#cfd0d3;margin-left:6px}
.thumb{position:absolute;width:45px;height:45px}

.comments{left:55px;top:782px;width:467px;height:154px}
.avatar{background:#e9e9e9;display:flex;align-items:center;justify-content:center}
.input{left:51px;top:16px;width:400px;height:26px;background:#fff;color:#555;font-size:6.5px;padding:9px 8px}
.post{left:406px;top:57px;width:45px;height:14px;line-height:14px;font-size:6.5px}
.comments .count{left:16px;top:88px;font-size:6.8px;font-weight:700}
.comments .sort{left:428px;top:88px;font-size:6.8px;font-weight:700}
.comments .rule{left:0;top:103px;width:467px;height:1px;background:var(--line)}
.comments .author{left:50px;top:112px;font-size:6.5px;color:#d8d9dc}
.comments .author span{color:var(--green)}
.comments .text{left:50px;top:130px;font-size:7px}
.comments .reply{left:433px;top:130px;font-size:6.5px;color:#cfd0d3;text-decoration:underline}

.related{left:0;top:968px;width:738px;height:30px;background:var(--bg-bar)}
.related .label{left:55px;top:10px;font-size:8px}
.related-strip{left:0;top:998px;width:738px;height:110px;background:var(--bg-dark)}

.footer{left:0;top:1108px;width:738px;height:92px;background:var(--bg-bar)}
.footer .wordmark{left:55px;top:31px;font-size:13px}
.footer .copy{left:55px;top:52px;font-size:5.5px;color:var(--dim)}
.fcol{top:22px;font-size:6.8px;line-height:15px}
.fcol h4{font-size:7px;font-weight:800;margin-bottom:3px;line-height:11px}
.email{left:498px;top:18px;width:100px;height:16px;background:#fff;color:#555;font-size:6.5px;padding:4px 8px}
.subscribe{left:612px;top:18px;width:70px;height:16px;line-height:16px;font-size:7px}
</style>
</head>
<body>

<header class="abs header">
  <div class="abs nav" style="left:55px">About Us</div>
  <div class="abs sep"></div>
  <div class="abs nav" style="left:104px">Contact Us</div>
  <div class="abs wordmark"><span class="mark"></span>PLNT VRSE</div>
  <div class="abs nav" style="left:588px">Login</div>
  <div class="abs btn signup">Sign Up</div>
</header>

<section class="abs gallery">
  <div class="tile part" style="left:0;top:5px;background:linear-gradient(#4a4a4a,#2a2a2a)" role="img" aria-label="Grey seaside photo, cropped"></div>
  <div class="tile" style="left:55px;top:5px;background:linear-gradient(135deg,#d8d8d8,#8a8a8a)" role="img" aria-label="Black and white photo of an accordion player by a window"></div>
  <div class="tile" style="left:161px;top:5px;background:linear-gradient(135deg,#3f9c94,#1d5a5c)" role="img" aria-label="Turquoise sea waves over rocks"></div>
  <div class="tile" style="left:266px;top:5px;background:linear-gradient(180deg,#7f9dc2,#c9dbe0 55%,#5d7d5a)" role="img" aria-label="Tropical beach with palm trees"></div>
  <div class="tile" style="left:372px;top:5px;background:linear-gradient(135deg,#b5651e,#3b2512)" role="img" aria-label="Wooden letterpress type blocks"></div>
  <div class="tile" style="left:477px;top:5px;background:linear-gradient(180deg,#3e3a3c,#6e5f4e 40%,#5c4c3c)" role="img" aria-label="Lifeguard hut on a sandy beach"></div>
  <div class="tile" style="left:582px;top:5px;background:linear-gradient(135deg,#6f8f3a,#9c3f80 50%,#5f8a35)" role="img" aria-label="Purple lilac blossoms"></div>
  <div class="tile part" style="left:688px;top:5px;background:#3a3b3d" role="img" aria-label="Next photo, cropped"></div>

  <div class="tile part" style="left:0;top:111px;background:linear-gradient(90deg,#2a2a2a,#4d4d4d)" role="img" aria-label="Dark photo, cropped"></div>
  <div class="arrow" style="left:14px;top:152px">&#8249;</div>
  <div class="tile" style="left:55px;top:111px;background:linear-gradient(135deg,#b36e55,#7a4838)" role="img" aria-label="Red rooftops of a dense city"></div>
  <div class="tile" style="left:161px;top:111px;background:linear-gradient(180deg,#e5e7ea,#8a9096)" role="img" aria-label="City skyline with skyscrapers"></div>
  <div class="tile" style="left:266px;top:111px;background:linear-gradient(135deg,#6f8a70,#3a5d6a)" role="img" aria-label="Bicycle handlebar over a river valley"></div>
  <div class="tile card" style="left:372px;top:111px">
    <div class="abs type"><svg width="8" height="7" viewBox="0 0 8 7"><rect x="0" y="1" width="8" height="6" rx="1" fill="#1a1a1a"/><circle cx="4" cy="4" r="1.5" fill="#21b36b"/></svg><span>Videos</span></div>
    <div class="abs name">Content Name</div>
    <div class="abs by">by Author Name</div>
    <div class="abs date">20.20.2017</div>
    <div class="abs icons"><span>$</span>
      <svg width="8" height="6" viewBox="0 0 8 6"><ellipse cx="4" cy="3" rx="3.6" ry="2.5" fill="none" stroke="#111" stroke-width="1"/><circle cx="4" cy="3" r="1.1" fill="#111"/></svg>
      <svg width="7" height="6" viewBox="0 0 10 9"><path d="M5 9 L0.8 4.6 A2.5 2.5 0 0 1 5 1.6 A2.5 2.5 0 0 1 9.2 4.6 Z" fill="#111"/></svg>
    </div>
  </div>
  <div class="tile" style="left:477px;top:111px;background:linear-gradient(180deg,#9bb3c3,#2f5246 50%,#1e3a38)" role="img" aria-label="Forested mountains above a lake"></div>
  <div class="tile" style="left:582px;top:111px;background:#9a9a9a" role="img" aria-label="Photo placeholder"></div>
  <div class="tile part" style="left:688px;top:111px;background:#3a3b3d" role="img" aria-label="Next photo, cropped"></div>
  <div class="arrow" style="left:716px;top:152px">&#8250;</div>

  <div class="tile part" style="left:0;top:216px;background:linear-gradient(180deg,#5a4630,#251c14)" role="img" aria-label="Palm trees at sunset, cropped"></div>
  <div class="tile" style="left:55px;top:216px;background:linear-gradient(180deg,#c5d3d4,#6f8f8c 60%,#4e6c6a)" role="img" aria-label="Harbour building by the water"></div>
  <div class="tile" style="left:161px;top:216px;background:linear-gradient(160deg,#d07a9c,#5a2f66 55%,#1f1838)" role="img" aria-label="Pink clouds at dusk with an aeroplane"></div>
  <div class="tile" style="left:266px;top:216px;background:linear-gradient(135deg,#b08a3a,#4a3a1c)" role="img" aria-label="Autumn tree with string lights"></div>
  <div class="tile" style="left:372px;top:216px;background:linear-gradient(180deg,#f2f2f2,#c9c9c9 60%,#555)" role="img" aria-label="Mountain peak in fog"></div>
  <div class="tile" style="left:477px;top:216px;background:linear-gradient(135deg,#c3d1db,#8ea4b3)" role="img" aria-label="Footprints in snow"></div>
  <div class="tile" style="left:582px;top:216px;background:#9a9a9a" role="img" aria-label="Photo placeholder"></div>
  <div class="tile part" style="left:688px;top:216px;background:#3a3b3d" role="img" aria-label="Next photo, cropped"></div>
</section>

<nav class="abs tabs">
  <div class="abs tab active" style="left:63px">All</div>
  <div class="abs tab-line"></div>
  <div class="abs tab" style="left:97px">Videos</div>
  <div class="abs tab" style="left:139px">Audios</div>
  <div class="abs tab" style="left:182px">Images</div>
  <div class="abs search">
    <svg class="abs" style="right:5px;top:3px" width="9" height="9" viewBox="0 0 10 10"><circle cx="4" cy="4" r="3" fill="none" stroke="#333" stroke-width="1.4"/><path d="M6.3 6.3 L9 9" stroke="#333" stroke-width="1.4"/></svg>
  </div>
</nav>

<article class="abs panel main">
  <div class="abs meta">by Author Name</div>
  <div class="dots" style="left:86px;top:10px"><span class="dot"></span><span class="dot"></span><span class="dot"></span></div>
  <div class="abs meta" style="left:413px">20.20.2017</div>
  <div class="abs video" role="img" aria-label="Video still of a calm sea under a blue sky"></div>
  <div class="abs play"><svg width="40" height="40" viewBox="0 0 40 40"><path d="M15 12 L28 20 L15 28 Z" fill="#fff"/></svg></div>
  <h1 class="abs title">Content Name</h1>
  <div class="abs rule" style="top:325px"></div>
  <p class="abs desc">Fusce vehicula dolor arcu, sit amet blandit dolor mollis nec. Donec viverra eleifend lacus, vitae ullamcorper metus. Sed sollicitudin ipsum quis nunc sollicitudin ultrices. Donec euismod scelerisque ligula.</p>
  <div class="abs more">Show more</div>
</article>

<aside class="abs panel side">
  <div class="abs stats"><span>$50</span>
    <span style="display:flex;gap:3px;align-items:center;font-weight:400"><svg width="9" height="6" viewBox="0 0 8 6"><ellipse cx="4" cy="3" rx="3.6" ry="2.5" fill="none" stroke="#fff" stroke-width="1"/><circle cx="4" cy="3" r="1.1" fill="#fff"/></svg>100</span>
    <span style="display:flex;gap:3px;align-items:center;font-weight:400"><svg width="8" height="7" viewBox="0 0 10 9"><path d="M5 9 L0.8 4.6 A2.5 2.5 0 0 1 5 1.6 A2.5 2.5 0 0 1 9.2 4.6 Z" fill="#fff"/></svg>100</span>
  </div>
  <div class="abs rule" style="top:26px"></div>
  <div class="abs btn buy">BUY THIS CONTENT</div>
  <div class="abs rule" style="top:74px"></div>
  <div class="tag" style="left:10px;top:90px">Dog</div>
  <div class="tag" style="left:44px;top:90px">Cute</div>
  <div class="tag" style="left:79px;top:90px">Video</div>
  <div class="tag" style="left:10px;top:113px">Short</div>
  <div class="abs rule" style="top:144px"></div>
  <div class="abs action" style="left:10px"><span class="sq"><svg width="9" height="8" viewBox="0 0 10 9"><path d="M5 9 L0.8 4.6 A2.5 2.5 0 0 1 5 1.6 A2.5 2.5 0 0 1 9.2 4.6 Z" fill="#fff"/></svg></span>Love</div>
  <div class="abs action" style="left:70px"><span class="sq"><svg width="9" height="9" viewBox="0 0 10 10"><path d="M1 3 V9 H8 V6" fill="none" stroke="#fff" stroke-width="1.2"/><path d="M4 6 L9 1 M6 1 H9 V4" fill="none" stroke="#fff" stroke-width="1.2"/></svg></span>Share</div>
  <div class="abs rule" style="top:185px"></div>
  <div class="abs from">More from<span>Author Name</span></div>
  <div class="thumb" style="left:5px;top:212px;background:linear-gradient(180deg,#d88a6a,#3a2a30)" role="img" aria-label="Sunset over the sea"></div>
  <div class="thumb" style="left:55px;top:212px;background:linear-gradient(180deg,#8ab8d6,#d9d1bf)" role="img" aria-label="People on a sandy beach"></div>
  <div class="thumb" style="left:105px;top:212px;background:linear-gradient(180deg,#d8cdb0,#5a4a30)" role="img" aria-label="Sun over dune grass"></div>
  <div class="thumb" style="left:5px;top:262px;background:linear-gradient(135deg,#a8a098,#5a5450)" role="img" aria-label="Pebbles close up"></div>
  <div class="thumb" style="left:55px;top:262px;background:radial-gradient(circle at 50% 60%,#d07a30,#111 55%)" role="img" aria-label="Small fire at night"></div>
  <div class="thumb" style="left:105px;top:262px;background:linear-gradient(180deg,#5a8ac0,#1d4f8a 60%,#d8d4c8)" role="img" aria-label="Coastline with waves"></div>
  <div class="thumb" style="left:5px;top:312px;background:linear-gradient(180deg,#3f78b0,#a8c6d8 60%,#384a5a)" role="img" aria-label="Rocky shore under blue sky"></div>
  <div class="thumb" style="left:55px;top:312px;background:linear-gradient(180deg,#b9c4cc,#b89a60)" role="img" aria-label="Sandy dunes"></div>
  <div class="thumb" style="left:105px;top:312px;background:linear-gradient(180deg,#d0d4d8,#3a3c40)" role="img" aria-label="Smooth stones on a beach"></div>
</aside>

<section class="abs panel comments">
  <div class="abs avatar" style="left:16px;top:16px;width:26px;height:26px">
    <svg width="14" height="14" viewBox="0 0 14 14"><circle cx="7" cy="4" r="3.2" fill="#777"/><path d="M1 14 Q1 8.5 7 8.5 Q13 8.5 13 14 Z" fill="#777"/></svg>
  </div>
  <div class="abs input">Post Comment...</div>
  <div class="abs btn post">Post</div>
  <div class="abs count">1 Comment</div>
  <div class="abs sort">Last &#9662;</div>
  <div class="abs rule"></div>
  <div class="abs" style="left:16px;top:111px;width:26px;height:26px;background:linear-gradient(135deg,#6a6e70,#3a3d40)" role="img" aria-label="Commenter profile photo"></div>
  <div class="abs author"><span>Author</span> - 20.20.2017</div>
  <div class="abs text">Nice!</div>
  <div class="abs reply">Reply</div>
</section>

<div class="abs related">
  <div class="abs label">Related Contents</div>
  <svg class="abs" style="left:674px;top:10px" width="9" height="10" viewBox="0 0 9 10"><path d="M4.5 10 V1 M1 4.5 L4.5 1 L8 4.5" fill="none" stroke="#fff" stroke-width="1.2"/></svg>
</div>
<section class="abs related-strip">
  <div class="tile part" style="left:0;top:6px;background:linear-gradient(180deg,#3e3a3c,#5c4c3c)" role="img" aria-label="Beach photo, cropped"></div>
  <div class="arrow" style="left:14px;top:47px">&#8249;</div>
  <div class="tile" style="left:55px;top:6px;background:linear-gradient(135deg,#d8d8d8,#8a8a8a)" role="img" aria-label="Black and white photo of an accordion player by a window"></div>
  <div class="tile" style="left:161px;top:6px;background:linear-gradient(135deg,#3f9c94,#1d5a5c)" role="img" aria-label="Turquoise sea waves over rocks"></div>
  <div class="tile" style="left:266px;top:6px;background:linear-gradient(180deg,#7f9dc2,#c9dbe0 55%,#5d7d5a)" role="img" aria-label="Tropical beach with palm trees"></div>
  <div class="tile" style="left:372px;top:6px;background:linear-gradient(135deg,#b5651e,#3b2512)" role="img" aria-label="Wooden letterpress type blocks"></div>
  <div class="tile" style="left:477px;top:6px;background:linear-gradient(180deg,#3e3a3c,#6e5f4e 40%,#5c4c3c)" role="img" aria-label="Lifeguard hut on a sandy beach"></div>
  <div class="tile" style="left:582px;top:6px;background:linear-gradient(135deg,#6f8f3a,#9c3f80 50%,#5f8a35)" role="img" aria-label="Purple lilac blossoms"></div>
  <div class="tile part" style="left:688px;top:6px;background:linear-gradient(135deg,#d0d0d0,#7a7a7a)" role="img" aria-label="Black and white photo, cropped"></div>
  <div class="arrow" style="left:716px;top:47px">&#8250;</div>
</section>

<footer class="abs footer">
  <div class="abs wordmark"><span class="mark"></span>PLNT VRSE</div>
  <div class="abs copy">&copy; 2017 All rights reserved.</div>
  <div class="abs fcol" style="left:193px"><h4>COMPANY</h4>About Us<br>Contact Us<br>Help</div>
  <div class="abs fcol" style="left:280px"><h4>SOCIAL</h4>Cliptower<br>Friendwall<br>Chirpline</div>
  <div class="abs fcol" style="left:361px"><h4>POLICY</h4>Terms of Use<br>Privacy Policy</div>
  <div class="abs email">Enter your email...</div>
  <div class="abs btn subscribe">Subscribe</div>
</footer>

</body>
</html>
```